Business Card Design for a Personal Trainer

I need a business card design for my job as a personal trainer. It should have a unique, modern and exclusive design. On the front there should be only my logo with my name and my job. 0163/2918374 Tobias Kellinger Lindenfeldweg 14 80412 Munich Germany The most important contact information is the web adress. it can be bigger than the rest, but its not necessary. The card should be 8,5cmx5,5cm big. Font: Roboto. Colors: black, white, gray, 56c1ff.

```html
<!DOCTYPE html>
<html lang="de">
<head>
<meta charset="utf-8">
<title>Tobias Kellinger – Visitenkarte</title>
<link rel="stylesheet" href="https://fonts.googleapis.com/css2?family=Roboto:wght@300;400&family=Roboto+Condensed:wght@400&display=swap">
<style>
  :root {
    --stage: #333333;
    --card: #181818;
    --white: #ffffff;
    --grey: #9a9a9a;
    --accent: #56c1ff;
  }
  * { margin: 0; padding: 0; box-sizing: border-box; }
  html, body { width: 1200px; height: 800px; overflow: hidden; }
  body {
    background: var(--stage);
    font-family: "Roboto", Arial, sans-serif;
    position: relative;
  }
  .card {
    position: absolute;
    top: 192px;
    width: 237px;
    height: 414px;
    background: var(--card);
  }
  .card--front { left: 314px; }
  .card--back { left: 651px; }

  .brand {
    position: absolute;
    left: 0; right: 0;
    top: 218px;
    text-align: center;
    color: var(--white);
  }
  .brand__name {
    font-weight: 400;
    font-size: 19.5px;
    letter-spacing: 0.2px;
    line-height: 1;
  }
  .brand__role {
    margin: 6px auto 0;
    width: 170px;
    display: flex;
    align-items: center;
    gap: 4px;
    font-size: 8px;
    letter-spacing: 2.4px;
    line-height: 1;
  }
  .brand__role::before, .brand__role::after {
    content: "";
    flex: 1;
    height: 1px;
    background: var(--white);
  }

  .portrait {
    position: absolute;
    left: 50px;
    top: 27px;
    width: 136px;
    height: 136px;
    border-radius: 50%;
    background: radial-gradient(circle at 50% 80%, #3a3a3a 0 38%, var(--accent) 39%);
  }
  .person {
    position: absolute;
    left: 0; right: 0;
    top: 170px;
    text-align: center;
    color: var(--white);
  }
  .person__name { font-size: 19.5px; font-weight: 400; line-height: 1.1; }
  .person__web {
    font-family: "Roboto Condensed", Arial, sans-serif;
    font-size: 9px;
    margin-top: 4px;
  }

  .contact {
    position: absolute;
    left: 11px;
    top: 312px;
    list-style: none;
  }
  .contact__item {
    display: flex;
    align-items: center;
    height: 24px;
    margin-bottom: 8px;
    color: var(--grey);
    font-weight: 300;
    font-size: 10.5px;
    line-height: 1.2;
  }
  .contact__icon { width: 23px; height: 23px; margin-right: 8px; flex: none; }
</style>
</head>
<body>
  <section class="card card--front">
    <div class="brand">
      <div class="brand__name">TOBIAS KELLINGER</div>
      <div class="brand__role">PERSONAL TRAINER</div>
    </div>
  </section>

  <section class="card card--back">
    <div class="portrait" role="img" aria-label="Porträtfoto von Tobias Kellinger mit verschränkten Armen"></div>
    <div class="person">
      <div class="person__name">Tobias Kellinger</div>
      <div class="person__web">www.tobiaskellinger.de</div>
    </div>
    <ul class="contact">
      <li class="contact__item">
        <svg class="contact__icon" viewBox="0 0 24 24" aria-hidden="true">
          <circle cx="12" cy="12" r="11" fill="none" stroke="#56c1ff" stroke-width="1.2"/>
          <path d="M8.5 7.5c.6-.6 1.3-.5 1.6.1l1 1.7c.3.5.1 1-.3 1.3l-.6.5c.5 1.2 1.5 2.3 2.7 2.8l.5-.6c.3-.4.9-.6 1.3-.3l1.7 1c.6.3.7 1 .1 1.6l-.7.7c-2.8 1-8.3-4.4-7.3-7.3z" fill="#bdbdbd"/>
        </svg>
        0163/2918374
      </li>
      <li class="contact__item">
        <svg class="contact__icon" viewBox="0 0 24 24" aria-hidden="true">
          <circle cx="12" cy="12" r="11" fill="none" stroke="#56c1ff" stroke-width="1.2"/>
          <rect x="6.5" y="8.5" width="11" height="7" fill="#bdbdbd"/>
          <path d="M6.5 8.5l5.5 4 5.5-4" fill="none" stroke="#181818" stroke-width="1"/>
        </svg>
        t.kellinger@postfeld.de
      </li>
      <li class="contact__item">
        <svg class="contact__icon" viewBox="0 0 24 24" aria-hidden="true">
          <circle cx="12" cy="12" r="11" fill="none" stroke="#56c1ff" stroke-width="1.2"/>
          <path d="M12 6.5a3.6 3.6 0 0 0-3.6 3.6c0 2.7 3.6 7 3.6 7s3.6-4.3 3.6-7A3.6 3.6 0 0 0 12 6.5z" fill="#bdbdbd"/>
          <circle cx="12" cy="10.1" r="1.3" fill="#181818"/>
        </svg>
        <span>Lindenfeldweg 14<br>80412 München</span>
      </li>
    </ul>
  </section>
</body>
</html>
```